Pellmor Brochure

We need a brochure design for a new company based in Chicago called "Pellmor" We are a innovative On-Demand Cleaning company. web site and APP based ordering for Cleaning service. Our product is you need a Cleaner (Maid) we only use the term Cleaner we send one in the area to you for cleaning. All of our cleaners are professionals and certified and put through a third party security clearance check before entering your property.

Our company works like ZOLT.. we are truly On-Demand when you need us for home, small office and New Construction cleanings.

We work with relators, Condo associations, Apartment Complexes and Corporate apartment company's.

```html
<!DOCTYPE html>
<html lang="en">
<head>
<meta charset="utf-8">
<title>Pellmor Brochure</title>
<link href="https://fonts.googleapis.com/css2?family=Montserrat:wght@400;500;600&family=Lato:ital,wght@1,700&family=Arimo:wght@400;700&display=swap" rel="stylesheet">
<style>
  :root {
    --paper: #f4f2ee;
    --lime: #c3dc6e;
    --lime-light: #e7f0c9;
    --green: #6cb344;
    --green-dark: #5aa038;
    --tagline: #a9cf5a;
    --ink: #1d1d1d;
    --white: #ffffff;
  }
  * { margin: 0; padding: 0; box-sizing: border-box; }
  html, body { width: 927px; height: 1200px; overflow: hidden; }
  body { font-family: "Arimo", Arial, sans-serif; color: var(--ink); }

  .brochure {
    position: relative;
    width: 927px;
    height: 1200px;
    background: var(--lime);
    overflow: hidden;
  }

  /* Header */
  .masthead {
    position: absolute; left: 0; top: 0;
    width: 927px; height: 227px;
    background: var(--paper);
  }
  .brand-mark {
    position: absolute; left: 55px; top: 24px;
    width: 180px; height: 180px;
    border-radius: 50%;
    border: 10px solid var(--tagline);
  }
  .brand-name {
    position: absolute; left: 262px; top: 46px;
    font-family: "Montserrat", sans-serif;
    font-weight: 500;
    font-size: 92px;
    letter-spacing: 10px;
    line-height: 1;
    color: var(--green);
  }
  .tagline {
    position: absolute; left: 294px; top: 136px;
    font-family: "Lato", sans-serif;
    font-style: italic;
    font-weight: 700;
    font-size: 37px;
    letter-spacing: 2.5px;
    color: var(--tagline);
  }
  .lamp { position: absolute; left: 228px; top: 222px; }

  /* Stats row */
  .stat-strip {
    position: absolute; left: 53px; top: 296px;
    width: 470px; height: 106px;
    border: 7px solid var(--green);
    background: var(--lime);
    display: flex;
  }
  .stat {
    display: flex; align-items: center;
    padding-left: 8px;
  }
  .stat + .stat { border-left: 7px solid var(--green); }
  .stat-days { width: 167px; }
  .stat-hours { flex: 1; }
  .stat-number {
    font-family: "Montserrat", sans-serif;
    font-weight: 500;
    font-size: 104px;
    line-height: 1;
    color: var(--white);
    letter-spacing: -3px;
  }
  .stat-label {
    font-family: "Montserrat", sans-serif;
    font-weight: 500;
    font-size: 21px;
    line-height: 1.25;
    color: var(--white);
    margin-left: 6px;
    align-self: flex-start;
    margin-top: 6px;
  }
  .guarantee {
    position: absolute; left: 516px; top: 281px;
    width: 360px; height: 157px;
    border: 7px solid var(--green);
    background: var(--lime-light);
    padding: 8px 0 0 14px;
  }
  .guarantee-number {
    font-family: "Montserrat", sans-serif;
    font-weight: 500;
    font-size: 98px;
    line-height: 1;
    color: var(--green-dark);
  }
  .guarantee-label {
    font-family: "Montserrat", sans-serif;
    font-weight: 500;
    font-size: 23px;
    color: var(--green-dark);
    margin: 6px 0 0 20px;
  }

  /* Intro card */
  .intro-card {
    position: absolute; left: 61px; top: 530px;
    width: 842px; height: 440px;
    border: 8px solid var(--green);
    border-radius: 24px;
    background: linear-gradient(180deg, #fbfdf5 0%, #eef5d8 45%, #d4e79a 100%);
  }
  .intro-heading {
    position: absolute; left: 240px; top: 30px; width: 520px;
    text-align: center;
    font-family: "Arimo", Arial, sans-serif;
    font-weight: 700;
    font-size: 31px;
    line-height: 1.3;
  }
  .intro-divider {
    position: absolute; left: 0; right: 0; top: 178px;
    border-top: 2px dashed #555;
  }
  .intro-body {
    position: absolute; left: 40px; top: 206px; width: 770px;
    font-size: 22.5px;
    line-height: 1.38;
    color: #2a2a2a;
  }
  .intro-body p + p { margin-top: 30px; }

  .portrait {
    position: absolute; left: 49px; top: 443px;
    width: 266px; height: 266px;
    border-radius: 50%;
    border: 6px solid var(--white);
    background: radial-gradient(circle at 50% 40%, #e9ddd2 0%, #b9a69a 55%, #5a4a44 100%);
  }

  /* Social + web */
  .social {
    position: absolute; left: 672px; top: 986px;
    display: flex; gap: 27px;
  }
  .social-dot {
    width: 56px; height: 56px; border-radius: 50%;
    background: var(--green);
  }
  .web-address {
    position: absolute; left: 676px; top: 1042px;
    font-size: 31px;
    color: var(--green);
  }

  /* Contact */
  .contact {
    position: absolute; left: 61px; top: 1052px;
    width: 323px; height: 160px;
    background: var(--white);
    border-radius: 16px 16px 0 0;
    text-align: center;
  }
  .contact-title {
    font-size: 28px;
    font-weight: 400;
    padding-top: 16px;
    padding-bottom: 10px;
    border-bottom: 5px solid var(--green);
    letter-spacing: 0.5px;
  }
  .contact-lines {
    font-weight: 700;
    font-size: 22.5px;
    line-height: 1.55;
    padding-top: 10px;
  }
</style>
</head>
<body>
<main class="brochure">
  <header class="masthead">
    <div class="brand-mark"></div>
    <div class="brand-name">PELLMOR</div>
    <div class="tagline">Cleaning You Can Trust</div>
  </header>
  <svg class="lamp" width="62" height="50" viewBox="0 0 62 50" aria-hidden="true">
    <rect x="27" y="0" width="8" height="26" fill="#6cb344"/>
    <path d="M3 48 A28 26 0 0 1 59 48 Z" fill="#6cb344"/>
  </svg>

  <section class="stat-strip">
    <div class="stat stat-days">
      <span class="stat-number">7</span>
      <span class="stat-label">DAYS<br>A<br>WEEK</span>
    </div>
    <div class="stat stat-hours">
      <span class="stat-number">24</span>
      <span class="stat-label">HOURS<br>A<br>DAY</span>
    </div>
  </section>
  <section class="guarantee">
    <div class="guarantee-number">100%</div>
    <div class="guarantee-label">GUARUNTEED</div>
  </section>

  <section class="intro-card">
    <h1 class="intro-heading">Pellmor is the premier, next-generation cleaning company.</h1>
    <div class="intro-divider"></div>
    <div class="intro-body">
      <p>We offer on-demand hourly cleaning services at the touch of a button, we’re available 24/7/and our bonded, insured cleaners are the best in the business.</p>
      <p>Starting here in Chicago, Pellmor is expanding to 13 cities nationwide, with collectively over 20 years of experience in the Service and Cleaning Industry</p>
    </div>
  </section>
  <div class="portrait" role="img" aria-label="Photo of a smiling cleaner in an apron"></div>

  <nav class="social" aria-label="Social links">
    <span class="social-dot"></span>
    <span class="social-dot"></span>
    <span class="social-dot"></span>
  </nav>
  <div class="web-address">pellmor.com</div>

  <section class="contact">
    <h2 class="contact-title">CONTACT US!</h2>
    <div class="contact-lines">info@pellmor.com<br>312-555-0148</div>
  </section>
</main>
</body>
</html>
```